Real Estate Agency Facebook Cover Photo

We need a Facebook cover photo created for our Real Estate Business. We also need this cover photo adapted to several other platforms. Please read this google doc for full specifications of the job https://papers.vellomarsh.com/sheet/d/8QwPzLk3RtYvB2nHs7JxVaM5_cEdGoUfNpLkZrWbYq/view?mode=shared

Please also carefully read the Must Haves/Should Not Haves

Please contact me if you have any queries. Looking forward to seeing your designs!

Doran

Industry/Entity Type

Real Estate Agent

Requirements
Must have
• The Taglines 'More Money In Your Pocket' and sub tagline 'With Our Low Flat Fee To Sell Your Home'

It can then also have other elements e.g our logo, contact details and anything else you think will work well.

It must also have great graphic design work which looks custom and very clean/modern
Should not have
• Must not have poor quality stock images or anything tacky regarding money etc

```html
<!DOCTYPE html>
<html lang="en">
<head>
<meta charset="utf-8">
<title>Norvale Cover – More Money In Your Pocket</title>
<link rel="stylesheet" href="https://fonts.googleapis.com/css2?family=Montserrat:wght@800&family=Questrial&display=swap">
<style>
  :root {
    --page-bg: #e9ebee;
    --cover-dark: #141414;
    --cover-mid: #1f1f1f;
    --cover-light: #2a2a2a;
    --text-white: #ffffff;
    --accent-red: #e0141e;
  }
  * { margin: 0; padding: 0; box-sizing: border-box; }
  html, body {
    width: 1002px;
    height: 1200px;
    overflow: hidden;
    background: var(--page-bg);
  }
  .canvas {
    width: 1002px;
    height: 1200px;
    display: flex;
    align-items: center;
    justify-content: center;
  }
  .cover {
    position: relative;
    width: 1002px;
    height: 373px;
    background:
      linear-gradient(135deg, var(--cover-mid) 0%, var(--cover-dark) 35%, var(--cover-dark) 60%, var(--cover-light) 100%);
    color: var(--text-white);
    text-align: center;
    overflow: hidden;
  }
  .cover__headline {
    position: absolute;
    left: 0; right: 0;
    top: 118px;
    font-family: "Montserrat", sans-serif;
    font-weight: 800;
    font-size: 41px;
    letter-spacing: 0.3px;
    line-height: 1;
  }
  .cover__subline {
    position: absolute;
    left: 0; right: 0;
    top: 180px;
    font-family: "Questrial", sans-serif;
    font-size: 27px;
    line-height: 1;
  }
  .cover__contact {
    position: absolute;
    left: 0; right: 0;
    top: 244px;
    display: flex;
    justify-content: center;
    align-items: center;
    gap: 18px;
    font-family: "Questrial", sans-serif;
    font-size: 19px;
    letter-spacing: 0.4px;
  }
  .contact-item {
    display: flex;
    align-items: center;
    gap: 9px;
  }
  .contact-icon { width: 20px; height: 20px; display: block; }
</style>
</head>
<body>
  <main class="canvas">
    <section class="cover">
      <h1 class="cover__headline">More Money In Your Pocket</h1>
      <p class="cover__subline">With our Low Flat Fee To Sell Your Home</p>
      <div class="cover__contact">
        <span class="contact-item">
          <svg class="contact-icon" viewBox="0 0 20 20" aria-hidden="true">
            <circle cx="10" cy="10" r="9.5" fill="var(--accent-red)"/>
            <g fill="none" stroke="var(--cover-dark)" stroke-width="1">
              <ellipse cx="10" cy="10" rx="4" ry="9.5"/>
              <line x1="0.5" y1="10" x2="19.5" y2="10"/>
              <line x1="2" y1="5.5" x2="18" y2="5.5"/>
              <line x1="2" y1="14.5" x2="18" y2="14.5"/>
              <line x1="10" y1="0.5" x2="10" y2="19.5"/>
            </g>
          </svg>
          www.norvale.com.au
        </span>
        <span class="contact-item">
          <svg class="contact-icon" viewBox="0 0 20 20" aria-hidden="true">
            <path fill="var(--accent-red)" d="M4.2 1.2 l3 3.4 c.5.6.4 1.4-.1 1.9 l-1.3 1.2 c1 2.3 2.7 4.1 5 5.2 l1.3-1.3 c.5-.5 1.3-.6 1.9-.1 l3.4 3 c.6.5.6 1.4 0 2 l-1.4 1.5 c-.8.8-2 1.1-3.1.7 C7.5 17 3 12.5 1.3 6.3 c-.3-1.1 0-2.3.8-3.1 L3.6 1.8 c.2-.3.4-.6.6-.6z"/>
          </svg>
          +12345098761
        </span>
      </div>
    </section>
  </main>
</body>
</html>
```